Business card for exciting VC company

Should look simple, crisp, and modern.

Industry/Entity Type

Venture Capital

Contact Information for Business Card

Would like to see at least one design that has our blue on the back with the tagline "Transforming Traditional Industry" and white front with contact details.

Font styles to use
Sans Serif

Requirements
Must have
• Logo

Gregory Tallis
gtallis@brindlewave.vc
Managing Partner
M (628)354-xxxx

```html
<!DOCTYPE html>
<html lang="en">
<head>
<meta charset="utf-8">
<title>Brindlewave Capital – Business Card</title>
<link rel="stylesheet" href="https://fonts.googleapis.com/css2?family=Lato:wght@400;700&display=swap">
<style>
  :root {
    --backdrop: #2b2b2d;
    --card-black: #050607;
    --card-white: #ffffff;
    --ink: #111111;
    --brand-blue: #3a7fd0;
    --paper-shade: #f1f1f1;
  }
  * { box-sizing: border-box; margin: 0; padding: 0; }
  html, body {
    width: 1200px;
    height: 1021px;
    overflow: hidden;
    background: var(--backdrop);
    font-family: "Lato", sans-serif;
  }
  .canvas {
    width: 1200px;
    height: 1021px;
    display: flex;
    flex-direction: column;
    align-items: center;
    justify-content: center;
    gap: 44px;
  }
  .card {
    width: 760px;
    height: 434px;
    position: relative;
    box-shadow: 0 14px 30px rgba(0,0,0,0.45);
  }
  .card-back {
    background: var(--card-black);
    color: var(--card-white);
  }
  .card-front {
    background: linear-gradient(180deg, var(--card-white) 55%, var(--paper-shade) 100%);
    color: var(--ink);
  }
  .tagline {
    position: absolute;
    top: 150px;
    left: 0;
    right: 0;
    text-align: center;
    font-weight: 700;
    font-size: 19px;
    letter-spacing: 0.04em;
    text-transform: uppercase;
  }
  .wordmark {
    display: flex;
    align-items: center;
    gap: 12px;
    font-weight: 700;
    letter-spacing: 0.08em;
    text-transform: uppercase;
  }
  .wordmark-square {
    width: 14px;
    height: 14px;
    background: var(--brand-blue);
    flex: none;
  }
  .card-back .wordmark {
    position: absolute;
    bottom: 70px;
    left: 50%;
    transform: translateX(-50%);
    font-size: 22px;
    white-space: nowrap;
  }
  .card-front .wordmark {
    position: absolute;
    top: 86px;
    right: 60px;
    font-size: 26px;
    white-space: nowrap;
  }
  .contact-block {
    position: absolute;
    left: 60px;
    top: 150px;
  }
  .person-name {
    color: var(--brand-blue);
    font-weight: 700;
    font-size: 21px;
  }
  .person-role {
    font-size: 20px;
    margin-top: 2px;
  }
  .accent-rule {
    width: 36px;
    height: 2px;
    background: var(--brand-blue);
    margin: 18px 0 26px;
  }
  .contact-list {
    list-style: none;
    font-size: 19px;
    line-height: 1.35;
  }
  .contact-list li {
    display: flex;
    align-items: center;
    gap: 8px;
  }
  .contact-icon {
    width: 18px;
    height: 18px;
    flex: none;
    stroke: var(--brand-blue);
    fill: none;
    stroke-width: 1.5;
  }
</style>
</head>
<body>
<main class="canvas">
  <section class="card card-back" aria-label="Card back">
    <p class="tagline">Transforming Traditional Industry</p>
    <div class="wordmark"><span class="wordmark-square"></span>Brindlewave Capital</div>
  </section>

  <section class="card card-front" aria-label="Card front">
    <div class="contact-block">
      <p class="person-name">Gregory Tallis</p>
      <p class="person-role">Managing Partner</p>
      <div class="accent-rule"></div>
      <ul class="contact-list">
        <li>
          <svg class="contact-icon" viewBox="0 0 18 18"><rect x="5" y="1.5" width="8" height="15" rx="1.5"/><line x1="8" y1="14" x2="10" y2="14"/></svg>
          (628) 354-xxxx
        </li>
        <li>
          <svg class="contact-icon" viewBox="0 0 18 18"><rect x="1.5" y="4" width="15" height="10"/><polyline points="1.5,4 9,10 16.5,4"/></svg>
          gtallis@brindlewave.vc
        </li>
        <li>
          <svg class="contact-icon" viewBox="0 0 18 18"><circle cx="9" cy="9" r="7"/><ellipse cx="9" cy="9" rx="3" ry="7"/><line x1="2" y1="9" x2="16" y2="9"/></svg>
          www.brindlewave.vc
        </li>
      </ul>
    </div>
    <div class="wordmark"><span class="wordmark-square"></span>Brindlewave Capital</div>
  </section>
</main>
</body>
</html>
```